Brookvane Counsel Partners Website Design

I need a website design for my new business consulting and executive coaching firm, Brookvane Counsel Partners. We provide consultative services to business C-suites as well as personal coaching to executives. I have attached the logo with color scheme I have chosen. I would like the website to reflect professionalism and continue the color scheme in the logo.

Target Market(s)

Small to medium business and their executives; middle to upper income men and women in mid- to late career looking for significance

Industry/Entity Type

Business Consultant

Number of Pages Required

4 page

Requirements
Must have
• A homepage with prominent logo and way to contact for more information; an area on the homepage with easy to read, clear text to describe what the company does; a prominent area on the homepage for a tagline; a blog page that can be updated regularly, an "about us" page with biographical information; an "about us" page; a page detailing services offered
• The web design must match the logo colors and font that I have uploaded.
Nice to have
• A lighthouse picture in the background or header
Should not have
• A lot of text area on the homepage

```html
<!DOCTYPE html>
<html lang="en">
<head>
<meta charset="utf-8">
<title>Brookvane Counsel Partners</title>
<link href="https://fonts.googleapis.com/css2?family=PT+Serif:wght@400;700&family=Open+Sans:wght@400;600;700&display=swap" rel="stylesheet">
<style>
:root{
  --navy:#1f3a6e;
  --navy-deep:#16294f;
  --red:#b3222b;
  --grey-text:#6b6f76;
  --footer:#2e2f31;
  --footer-bar:#1f2022;
  --white:#ffffff;
  --tile-grey:#7c8189;
  --tile-dark:#3a3d42;
  --tile-blue:#2c4c86;
  --tile-red:#9d2a33;
}
*{box-sizing:border-box;margin:0;padding:0}
html,body{width:684px;height:1200px;overflow:hidden;background:#fff}
body{font-family:"Open Sans",Arial,sans-serif;color:var(--grey-text);position:relative}
.serif{font-family:"PT Serif",Georgia,serif}

/* Header */
.site-header{position:absolute;top:0;left:0;width:684px;height:68px;background:var(--white);display:flex;align-items:center;justify-content:space-between;padding:0 28px}
.brand{display:flex;align-items:center;gap:8px}
.brand-square{width:18px;height:18px;background:var(--navy)}
.brand-name{font-family:"PT Serif",Georgia,serif;font-weight:700;font-size:13px;color:var(--navy);letter-spacing:.5px;line-height:1.1}
.main-nav{display:flex;gap:32px}
.main-nav a{font-size:10px;font-weight:600;color:#333;text-decoration:none;letter-spacing:.5px;padding-bottom:4px}
.main-nav a.active{color:var(--red);border-bottom:2px solid var(--red)}

/* Hero */
.hero{position:absolute;top:68px;left:0;width:684px;height:297px;background:linear-gradient(180deg,#4f6880 0%,#6d8398 45%,#3c4f63 100%);text-align:center;color:var(--white)}
.hero-brand{position:absolute;top:78px;left:0;width:100%;display:flex;justify-content:center;align-items:center;gap:8px}
.hero-brand .brand-square{background:var(--white)}
.hero-brand .brand-name{color:var(--white)}
.hero h1{position:absolute;top:122px;width:100%;font-family:"PT Serif",Georgia,serif;font-weight:400;font-size:25px;letter-spacing:.5px}
.hero-contact{position:absolute;top:162px;width:100%;font-size:11px;letter-spacing:.5px}
.btn-navy{position:absolute;top:186px;left:287px;width:110px;height:28px;background:var(--navy);color:var(--white);font-size:10px;font-weight:600;line-height:28px;letter-spacing:.5px}
.hero-dots{position:absolute;top:268px;left:0;width:100%;display:flex;justify-content:center;gap:10px}
.hero-dots span{width:8px;height:8px;border:1px solid var(--white);border-radius:50%}
.hero-dots span.on{background:var(--red);border-color:var(--red)}

/* Service tiles */
.services{position:absolute;top:365px;left:0;width:684px;height:195px;display:flex}
.service{flex:1;position:relative;padding:26px 14px 0 14px;color:var(--white)}
.service.grey{background:linear-gradient(160deg,#9ea3aa,var(--tile-grey))}
.service.dark{background:linear-gradient(160deg,#4a4e54,var(--tile-dark))}
.service.blue{background:linear-gradient(160deg,#3a5e9c,var(--tile-blue))}
.service.red{background:linear-gradient(160deg,#b23a44,var(--tile-red))}
.service-icon{width:36px;height:36px;border:2px solid var(--white);border-radius:50%;display:flex;align-items:center;justify-content:center;margin-bottom:10px}
.service h3{font-family:"PT Serif",Georgia,serif;font-weight:400;font-size:13px;line-height:1.2;letter-spacing:.5px;margin-bottom:6px}
.service p{font-size:9px;line-height:1.4;opacity:.9}

/* Welcome */
.welcome{position:absolute;top:560px;left:0;width:684px;height:225px;background:var(--white)}
.welcome-mark{position:absolute;top:40px;left:70px;width:130px;height:130px;background:var(--navy)}
.welcome-text{position:absolute;top:40px;left:280px;width:360px}
.welcome-text .kicker{font-family:"PT Serif",Georgia,serif;font-size:14px;color:var(--red)}
.welcome-text h2{font-family:"PT Serif",Georgia,serif;font-weight:700;font-size:16px;color:var(--navy);letter-spacing:.5px;margin:2px 0 8px}
.welcome-text p{font-size:9.5px;line-height:1.55}
.btn-outline{display:inline-block;margin-top:14px;border:1px solid var(--navy);color:var(--navy);font-size:9.5px;font-weight:600;padding:6px 18px;letter-spacing:.5px}

/* Inquiry */
.inquiry{position:absolute;top:785px;left:0;width:684px;height:240px;background:linear-gradient(180deg,#2d4d7e 0%,#3f5f8c 55%,#25406b 100%)}
.inquiry h2{position:absolute;top:52px;width:100%;text-align:center;font-family:"PT Serif",Georgia,serif;font-weight:400;font-size:20px;color:var(--white)}
.field{position:absolute;height:22px;background:rgba(20,40,75,.55);border:1px solid rgba(255,255,255,.45);color:rgba(255,255,255,.85);font-size:9px;padding:4px 8px}
.submit{position:absolute;top:150px;left:350px;width:294px;height:26px;background:var(--white);color:var(--navy);font-weight:700;font-size:11px;text-align:center;line-height:26px;letter-spacing:1px}

/* Footer */
.site-footer{position:absolute;top:1025px;left:0;width:684px;height:150px;background:var(--footer);color:#c9cbce;font-size:8.5px}
.site-footer h4{font-family:"PT Serif",Georgia,serif;font-weight:400;font-size:13px;color:var(--white);margin-bottom:10px}
.col{position:absolute;top:18px}
.post{display:flex;gap:8px;margin-bottom:10px;width:210px}
.avatar{width:24px;height:24px;border-radius:50%;background:#8a8d92;flex:none}
.post-body{flex:1;line-height:1.4}
.post-ago{color:#9a9da2;flex:none}
.links{display:grid;grid-template-columns:60px 60px;row-gap:5px}
.contact-row{display:flex;align-items:center;gap:8px;margin-bottom:8px}
.bottom-bar{position:absolute;top:1175px;left:0;width:684px;height:25px;background:var(--footer-bar);color:#b5b7ba;font-size:8.5px;display:flex;align-items:center;justify-content:space-between;padding:0 28px}
.social{display:flex;gap:8px}
.social span{width:9px;height:9px;border-radius:50%;background:#c9cbce}
</style>
</head>
<body>

<header class="site-header">
  <div class="brand"><span class="brand-square"></span><span class="brand-name">BROOKVANE<br>COUNSEL PARTNERS</span></div>
  <nav class="main-nav">
    <a class="active">HOME</a><a>ABOUT</a><a>SERVICES</a><a>CONTACT</a>
  </nav>
</header>

<section class="hero" role="img" aria-label="Lighthouse on a rocky coast under a cloudy sky">
  <div class="hero-brand"><span class="brand-square"></span><span class="brand-name">BROOKVANE<br>COUNSEL PARTNERS</span></div>
  <h1>BUSINESS IMPROVEMENT SPECIALIST</h1>
  <p class="hero-contact">CONTACT US ON - (0) 555 0192 384</p>
  <div class="btn-navy">KNOW MORE</div>
  <div class="hero-dots"><span class="on"></span><span></span><span></span></div>
</section>

<section class="services">
  <article class="service grey" role="img" aria-label="Business team planning at a table">
    <div class="service-icon"><svg width="18" height="18" viewBox="0 0 18 18"><path d="M3 15V9M8 15V5M13 15V2" stroke="#fff" stroke-width="2.5"/></svg></div>
    <h3>STRATEGY &amp;<br>PLANNING</h3>
    <p>Lorem Ipsum is simply<br>dummy text of the...</p>
  </article>
  <article class="service dark" role="img" aria-label="Laptop and documents on a desk">
    <div class="service-icon"><svg width="18" height="18" viewBox="0 0 18 18"><rect x="2" y="3" width="14" height="12" fill="none" stroke="#fff" stroke-width="2"/><path d="M2 7h14" stroke="#fff" stroke-width="2"/></svg></div>
    <h3>PROJECT<br>MANAGEMENT</h3>
    <p>Lorem Ipsum is simply<br>dummy text of the...</p>
  </article>
  <article class="service blue" role="img" aria-label="Charts and reports under review">
    <div class="service-icon"><svg width="18" height="18" viewBox="0 0 18 18"><circle cx="8" cy="8" r="5" fill="none" stroke="#fff" stroke-width="2"/><path d="M12 12l4 4" stroke="#fff" stroke-width="2.5"/></svg></div>
    <h3>OBJECTIVE<br>REVIEWS</h3>
    <p>Lorem Ipsum is simply<br>dummy text of the...</p>
  </article>
  <article class="service red" role="img" aria-label="Hands pointing at a printed chart">
    <div class="service-icon"><svg width="18" height="18" viewBox="0 0 18 18"><path d="M9 9V2a7 7 0 1 1-7 7z" fill="#fff"/></svg></div>
    <h3>BUSINESS<br>ANALYSIS</h3>
    <p>Lorem Ipsum is simply<br>dummy text of the...</p>
  </article>
</section>

<section class="welcome">
  <div class="welcome-mark"></div>
  <div class="welcome-text">
    <p class="kicker">Welcome to</p>
    <h2>BROOKVANE COUNSEL PARTNERS</h2>
    <p>Lorem Ipsum is simply dummy text of the printing and typesetting industry. Lorem Ipsum has been the industry's standard dummy text ever since the 1500s, when an unknown printer took a galley of type and scrambled it to make a type specimen book. It has survived not only five centuries.</p>
    <span class="btn-outline">KNOW MORE</span>
  </div>
</section>

<section class="inquiry" role="img" aria-label="Pier stretching over calm blue water">
  <h2>Send a Message For Inquiry</h2>
  <div class="field" style="top:95px;left:40px;width:296px">Your Name</div>
  <div class="field" style="top:122px;left:40px;width:296px">Your E-mail Address</div>
  <div class="field" style="top:149px;left:40px;width:296px;height:27px">Subject</div>
  <div class="field" style="top:95px;left:350px;width:294px;height:50px">Your Message Here</div>
  <div class="submit">SUBMIT</div>
</section>

<footer class="site-footer">
  <div class="col" style="left:28px">
    <h4>Blog</h4>
    <div class="post"><span class="avatar"></span><div class="post-body">Carla Denton posted a new blog<br>Today 3:40 pm - 12.06.2014</div><span class="post-ago">3m ago</span></div>
    <div class="post"><span class="avatar"></span><div class="post-body">Owen Marsh shared a new<br>Today 2:15 pm - 12.06.2014</div><span class="post-ago">2h ago</span></div>
  </div>
  <div class="col" style="left:295px">
    <h4>Navigation Links</h4>
    <div class="links"><span>Home</span><span>Clients</span><span>About</span><span>Blog</span><span>Services</span><span>Terms</span><span>Enquiry</span><span>Faqs</span><span>Contact</span></div>
  </div>
  <div class="col" style="left:455px">
    <h4>Contact us</h4>
    <div class="contact-row"><svg width="10" height="12" viewBox="0 0 10 12"><path d="M5 12S0 6.5 0 4.5a5 5 0 0 1 10 0C10 6.5 5 12 5 12z" fill="#c9cbce"/></svg><span>123 Street Name, Area, City, Country<br>Zipcode</span></div>
    <div class="contact-row"><svg width="10" height="10" viewBox="0 0 10 10"><path d="M1 1h3l1 2.5-1.5 1a6 6 0 0 0 2 2l1-1.5L9 6v3c-4.5 0-8-3.5-8-8z" fill="#c9cbce"/></svg><span>+(0) 555 0192 384</span></div>
    <div class="contact-row"><svg width="11" height="8" viewBox="0 0 11 8"><rect width="11" height="8" fill="#c9cbce"/><path d="M0 0l5.5 4.5L11 0" fill="none" stroke="#2e2f31"/></svg><span>info@brookvane.com</span></div>
  </div>
</footer>

<div class="bottom-bar">
  <span>© 2015 BROOKVANE. All Rights Reserved.</span>
  <div class="social"><span></span><span></span><span></span><span></span></div>
</div>

</body>
</html>
```